Course Graduation Certificate

This project is not for a flyer but instead for the creation of a course graduation certificate. The final certificate needs to include the Marlowe Summit Aviation Academy logo and the text stating as follows:
Certifies that ___________________________ has satisfactorily completed the course of _______________________________ on ________________________________
I would also like to include some type of gold seal of completion as well as a place to sign my name and credentials at the bottom of the certificate
I have included the Marlowe Summit Aviation Academy logo as well as three other certificate examples for you to work from.
Target Market(s)
Students completing a certification course and receiving a certificate
Look and feel

```html
<!DOCTYPE html>
<html lang="en">
<head>
<meta charset="utf-8">
<title>Certificate of Graduation — Marlowe Summit Aviation Academy</title>
<link rel="stylesheet" href="https://fonts.googleapis.com/css2?family=Cinzel:wght@400;500&family=Lora&display=swap">
<style>
  :root {
    --paper: #f1ede4;
    --paper-shade: #e8e2d5;
    --ink: #1c1b19;
    --frame-blue: #2f7fd3;
    --frame-blue-deep: #1c63b8;
    --frame-blue-light: #7fb2e6;
    --rule-gold: #e0a43a;
    --seal-gold: #f6c232;
    --seal-gold-deep: #e9a514;
  }
  * { box-sizing: border-box; margin: 0; padding: 0; }
  html, body { width: 1200px; height: 848px; overflow: hidden; }
  body {
    position: relative;
    background: radial-gradient(ellipse at 50% 45%, var(--paper) 55%, var(--paper-shade) 100%);
    font-family: "Cinzel", serif;
    color: var(--ink);
  }
  .border-band {
    position: absolute;
    left: 54px; top: 36px; width: 1092px; height: 777px;
    background:
      repeating-linear-gradient(90deg, var(--frame-blue) 0 3px, var(--frame-blue-light) 3px 5px),
      var(--frame-blue);
    background-blend-mode: multiply;
    border: 2px solid var(--frame-blue-deep);
  }
  .certificate-panel {
    position: absolute;
    left: 138px; top: 111px; width: 927px; height: 627px;
    background: radial-gradient(ellipse at 50% 45%, var(--paper) 60%, var(--paper-shade) 100%);
    border: 2px solid var(--frame-blue-deep);
    box-shadow: 0 0 0 4px var(--paper), 0 0 0 6px var(--frame-blue-deep);
  }
  .content { position: absolute; inset: 0; }
  .title {
    position: absolute; left: 0; width: 1200px; top: 124px;
    text-align: center; font-size: 79px; font-weight: 400; line-height: 1;
    letter-spacing: 1px;
    text-shadow: 3px 3px 0 rgba(0,0,0,0.18);
  }
  .subtitle {
    position: absolute; left: 0; width: 1192px; top: 198px;
    text-align: center; font-size: 30px; line-height: 1;
  }
  .divider { position: absolute; left: 480px; top: 246px; }
  .line-label {
    position: absolute; left: 0; width: 1200px;
    text-align: center; line-height: 1; text-transform: lowercase;
  }
  .certifies { top: 286px; font-size: 27px; text-transform: none; }
  .completed { top: 402px; font-size: 27px; letter-spacing: 0.6px; }
  .on-date { top: 500px; font-size: 27px; }
  .fill-rule { position: absolute; height: 1px; background: var(--rule-gold); }
  .rule-name { left: 326px; width: 548px; top: 378px; }
  .rule-course { left: 345px; width: 490px; top: 485px; }
  .rule-date { left: 345px; width: 548px; top: 572px; }
  .seal { position: absolute; left: 166px; top: 552px; }
  .academy-name {
    position: absolute; left: 440px; width: 320px; top: 652px;
    text-align: center; font-family: "Cinzel", serif; font-weight: 500;
    font-size: 19px; line-height: 1.25; color: var(--frame-blue-deep);
  }
  .signature {
    position: absolute; left: 817px; top: 669px; width: 214px;
    border-top: 1px solid var(--ink);
  }
  .signature-title {
    margin-top: 13px; margin-left: 4px;
    font-family: "Lora", serif; font-size: 19px;
  }
</style>
</head>
<body>
  <div class="border-band" role="img" aria-label="Ornate blue guilloche certificate border with scrollwork corner flourishes"></div>
  <div class="certificate-panel"></div>

  <main class="content">
    <h1 class="title">CERTIFICATE</h1>
    <p class="subtitle">OF GRADUATION</p>

    <svg class="divider" width="240" height="16" viewBox="0 0 240 16" aria-hidden="true">
      <line x1="6" y1="8" x2="84" y2="8" stroke="#1c1b19" stroke-width="1.2"/>
      <line x1="156" y1="8" x2="234" y2="8" stroke="#1c1b19" stroke-width="1.2"/>
      <circle cx="6" cy="8" r="2.5" fill="#1c1b19"/>
      <circle cx="234" cy="8" r="2.5" fill="#1c1b19"/>
      <ellipse cx="108" cy="8" rx="22" ry="5" fill="none" stroke="#1c1b19" stroke-width="1.2"/>
      <ellipse cx="132" cy="8" rx="22" ry="5" fill="none" stroke="#1c1b19" stroke-width="1.2"/>
    </svg>

    <p class="line-label certifies">This Certifies That</p>
    <div class="fill-rule rule-name"></div>

    <p class="line-label completed">has satisfactorily completed the course of</p>
    <div class="fill-rule rule-course"></div>

    <p class="line-label on-date">on</p>
    <div class="fill-rule rule-date"></div>

    <svg class="seal" width="110" height="160" viewBox="0 0 110 160" role="img" aria-label="Gold seal of completion">
      <polygon points="28,60 50,70 28,158 14,140 2,150" fill="#f6c232"/>
      <polygon points="82,60 60,70 82,158 96,140 108,150" fill="#f6c232"/>
      <circle cx="55" cy="48" r="49" fill="#e9a514"/>
      <circle cx="55" cy="48" r="37" fill="#f6c232" stroke="#fff6d8" stroke-width="2"/>
    </svg>

    <p class="academy-name">Marlowe Summit<br>Aviation Academy</p>

    <div class="signature">
      <p class="signature-title">President of Corp</p>
    </div>
  </main>
</body>
</html>
```